Digital agency needs new homepage design

We need to redesign our current homepage to illustrate better the end to end digital services we provide.

Our services in a nutshell:
Research- both about our client and their (potential) users.
Digital marketing – PPC, affiliate marketing, targeting.
Conversion optimization – A/B testing, dynamic content and personalisation.

The story-line:
Imagine you are a potential new client. Beginning a new adventure with you will include research. We will look at your current business and website. We will analyze your pain points, your current status in the market, where your users come from and what do they want. We will also look ahead into potential markets and users.

We will then design a campaign, based on our findings. This can be one of the many marketing services we offer or a few.

We will also optimize your current website. We make sure your users can find what they are looking for easier. We customize your landing pages to them. We ease their journey through your checkout.

Design Guidelines:
We’d like to keep the look & feel as it currently is on the current website.

Fonts are: Arial and Sans-serif
Logo attached

The new homepage wireframes are in Balsamiq format. In case you cannot open the file, a png of them is attached as well.

Also see our current homepage: http://www.wrenmoorquill.com

Reason: The designs are close but not yet complete. I will add feedback to each designer in order to refine the design.

Industry/Entity Type

Digital

Number of Pages Required

1 page

Font styles to use
Sans Serif

Requirements
Must have
• all modules within the wireframes
Nice to have
• Any suggestions welcome
Should not have
• keep the same look and feel as the current website: www.wrenmoorquill.com/

```html
<!DOCTYPE html>
<html lang="en">
<head>
<meta charset="utf-8">
<title>Wrenmoor Quill — Digital Services</title>
<link rel="stylesheet" href="https://fonts.googleapis.com/css2?family=Lato:wght@300;400;700&display=swap">
<style>
:root{
  --green:#5bbd6a;
  --green-dark:#3fa451;
  --green-soft:#e8f5ea;
  --ink:#222;
  --text:#555;
  --muted:#888;
  --line:#d8d8d8;
  --grey-bg:#efefef;
  --footer:#3a3a3a;
  --white:#fff;
}
*{box-sizing:border-box;margin:0;padding:0}
html,body{width:1200px;height:4061px;overflow:hidden}
body{position:relative;background:var(--white);font-family:'Lato',Arial,sans-serif;color:var(--text);font-size:13px}
.abs{position:absolute}
.ph{position:absolute}
.green{color:var(--green)}

/* header */
.site-header{position:absolute;left:0;top:0;width:1200px;height:82px;border-bottom:1px solid var(--line)}
.brand{position:absolute;left:150px;top:26px;font-size:22px;font-weight:700;letter-spacing:2px;color:var(--ink);text-transform:uppercase}
.nav{position:absolute;left:520px;top:30px;display:flex;gap:30px;font-size:13px;color:#444}
.nav .active{color:var(--green);border-bottom:2px solid var(--green);padding-bottom:6px}

/* hero */
.hero-tile{position:absolute;top:109px;width:286px;height:286px}
.hero-cap{position:absolute;top:404px;width:286px;text-align:center;font-size:17px;color:#333}
.rule{position:absolute;left:0;width:1200px;height:1px;background:#999}

h2.section-title{position:absolute;left:0;width:1200px;text-align:center;font-size:25px;font-weight:400;color:var(--ink);letter-spacing:1px;text-transform:uppercase}
.subtitle{position:absolute;left:0;width:1200px;text-align:center;font-size:14px;color:#444}

/* audience */
.aud-col h3{font-size:20px;font-weight:400;color:#333;margin-bottom:18px}
.aud-col p{font-size:13px;line-height:1.55;margin-bottom:14px;color:#555}
.slide-arrow{position:absolute;width:32px;height:32px;border-radius:3px;display:flex;align-items:center;justify-content:center}
.slide-arrow.g{background:var(--green)}
.slide-arrow.d{background:#333}

/* tools */
.tools-band{position:absolute;left:0;top:927px;width:1200px;height:286px;background:var(--grey-bg)}
.tool-card{position:absolute;top:55px;width:264px;height:172px}
.tool-cap{position:absolute;top:235px;width:264px;text-align:center;font-size:18px;color:#333}

/* traffic boxes */
.tbox{position:absolute;width:368px;border:1px solid var(--line);background:var(--white)}
.tbox-head{height:44px;line-height:44px;text-align:center;color:var(--green);font-size:16px;letter-spacing:.5px;text-transform:uppercase;border-bottom:3px solid #ddd;background:#fafafa}
.tbox ul{list-style:none;padding:16px 20px 0}
.tbox li{position:relative;padding-left:22px;font-size:12.5px;line-height:1.4;margin-bottom:14px;color:#444}
.tbox li::before{content:"";position:absolute;left:0;top:3px;width:11px;height:11px;border-radius:50%;background:var(--green)}
.learn{position:absolute;right:18px;bottom:12px;font-size:12px;font-weight:700;color:var(--green)}

/* chart */
.chart{position:absolute;left:150px;top:2112px;overflow:visible}
.callout{position:absolute;background:var(--green);color:#fff;font-size:13px;padding:7px 10px;border-radius:2px;white-space:nowrap}
.stats-box{position:absolute;left:196px;top:2112px;width:186px;height:169px;background:var(--green);padding:14px 14px;color:#fff;font-size:9.5px;line-height:1.35}
.stats-box p{position:relative;padding-left:14px;margin-bottom:10px}
.stats-box p::before{content:"";position:absolute;left:0;top:2px;width:7px;height:7px;border-radius:50%;background:#fff}
.stats-box b{font-size:11px;letter-spacing:.5px}

/* personalisation */
.pill{position:absolute;left:202px;width:103px;background:var(--green);color:#fff;text-align:center;font-size:13px;line-height:1.3;display:flex;align-items:center;justify-content:center;border-radius:2px}
.panel{position:absolute;left:376px;top:2516px;width:268px;height:318px;border:1px solid var(--green);padding:18px 18px}
.panel-title{background:var(--green);color:#fff;text-align:center;font-size:17px;padding:8px 0;margin:0 0 16px}
.panel p{font-size:11px;line-height:1.45;color:#666}
.persona{position:absolute;left:810px;width:185px;height:74px;border:1px solid var(--green);padding:8px}
.persona p{position:absolute;left:62px;top:8px;right:8px;font-size:10px;line-height:1.4;color:#666}

/* projects */
.projects-band{position:absolute;left:0;top:2896px;width:1200px;height:335px;background:var(--grey-bg)}
.projects-box{position:absolute;left:150px;top:3000px;width:900px;height:196px;background:var(--white);border:1px solid var(--line)}
.tab{position:absolute;left:169px;width:239px;height:38px;border:2px solid #555;font-size:14px;line-height:34px;padding-left:12px;color:#333;background:#fff}
.tab.active{background:var(--green);border-color:var(--green);color:#fff;width:254px}
.client{position:absolute;width:122px;height:76px;border:1px solid #e3e3e3;display:flex;align-items:center;justify-content:center;font-size:15px;font-weight:700;color:#333;text-align:center;line-height:1.1}

/* articles */
.article{position:absolute;width:436px;height:146px;border-bottom:1px solid var(--line)}
.article-body{position:absolute;left:10px;top:10px;width:250px;height:126px}
.article h4{font-size:14px;font-weight:400;color:#222;white-space:nowrap;margin-bottom:10px}
.article p{font-size:10.5px;line-height:1.5;color:#666}
.article .more{position:absolute;left:0;bottom:4px;font-size:11px;color:var(--green)}
.article .thumb{position:absolute;right:6px;top:8px;width:168px;height:128px}

/* cta */
.cta{position:absolute;left:0;top:3826px;width:1200px;height:169px;background:var(--green)}
.cta h3{position:absolute;left:622px;top:36px;font-size:28px;font-weight:400;color:#fff}
.cta .tag{position:absolute;left:626px;top:78px;font-size:12px;color:#eafbe9}
.cta .btn{position:absolute;left:586px;top:109px;width:169px;height:32px;background:#fff;color:var(--green-dark);font-size:11px;font-weight:700;letter-spacing:1px;line-height:32px;text-align:center;text-transform:uppercase}
.site-footer{position:absolute;left:0;top:3995px;width:1200px;height:66px;background:var(--footer);color:#bbb;font-size:11px}
.site-footer .copy{position:absolute;left:150px;top:26px}
.site-footer nav{position:absolute;right:150px;top:26px;display:flex;gap:14px}
</style>
</head>
<body>

<header class="site-header">
  <div class="brand">Wrenmoor Quill</div>
  <nav class="nav">
    <span class="active">Our Service</span><span>Service</span><span>Client Work</span><span>Resources</span><span>Events</span><span>Contact Us</span><span>Blog</span>
  </nav>
</header>

<!-- services hero -->
<div class="hero-tile" style="left:150px;background:linear-gradient(135deg,#9ec4e4,#d9e6ef)" role="img" aria-label="Photo of a researcher working at a computer"></div>
<div class="hero-tile" style="left:458px;background:linear-gradient(160deg,#0e2a3a,#3b6f85)" role="img" aria-label="Photo of a businessman holding a tablet with a glowing digital globe"></div>
<div class="hero-tile" style="left:766px;background:linear-gradient(135deg,#c9d1d6,#7f8e96)" role="img" aria-label="Photo of a hand sketching website wireframes on glass"></div>
<div class="hero-cap" style="left:150px">Research &nbsp;<svg width="20" height="10"><path d="M0 5h17M13 1l5 4-5 4" stroke="#333" stroke-width="2" fill="none"/></svg></div>
<div class="hero-cap" style="left:458px"><svg width="20" height="10"><path d="M20 5H3M7 1 2 5l5 4" stroke="#333" stroke-width="2" fill="none"/></svg>&nbsp; Digital Marketing &nbsp;<svg width="20" height="10"><path d="M0 5h17M13 1l5 4-5 4" stroke="#333" stroke-width="2" fill="none"/></svg></div>
<div class="hero-cap" style="left:766px"><svg width="20" height="10"><path d="M20 5H3M7 1 2 5l5 4" stroke="#333" stroke-width="2" fill="none"/></svg>&nbsp; Conversion Optimisation</div>
<div class="rule" style="top:445px"></div>

<!-- audience -->
<h2 class="section-title" style="top:480px">Finding and knowing your audiance</h2>
<div class="ph" style="left:464px;top:532px;width:300px;height:368px;border-radius:50%;background:radial-gradient(circle at 50% 45%,#d9f0dc 0 30%,#6fc57b 31% 36%,#fff 37%)" role="img" aria-label="Illustration of a magnifying glass over a ring of connected user figures"></div>
<div class="abs aud-col" style="left:190px;top:632px;width:190px;text-align:right">
  <h3 style="text-align:left;margin-left:96px">To Target</h3>
  <p>Your Brand Position In The Market</p>
  <p>Potential For Your Brand In New Market (Market Research)</p>
  <p>Consumer Behaviour On Your Site</p>
</div>
<div class="abs aud-col" style="left:826px;top:632px;width:200px">
  <h3>To Convert</h3>
  <p>Who Are Your User And Where Do How They Arrive At Your Site</p>
  <p>Their Intentions 'think' And 'feel' When They Land On Your Site</p>
  <p>What They Look For On Your Site</p>
</div>
<div class="slide-arrow g" style="left:58px;top:694px"><svg width="10" height="12"><path d="M8 1 2 6l6 5" stroke="#fff" stroke-width="2" fill="none"/></svg></div>
<div class="slide-arrow d" style="left:1108px;top:694px"><svg width="10" height="12"><path d="M2 1l6 5-6 5" stroke="#fff" stroke-width="2" fill="none"/></svg></div>

<!-- tools -->
<div class="tools-band">
  <svg class="abs" style="left:588px;top:-12px" width="24" height="24"><circle cx="12" cy="12" r="12" fill="#fff"/><path d="M7 10l5 5 5-5" stroke="#aaa" stroke-width="2" fill="none"/></svg>
  <div class="tool-card" style="left:164px;background:linear-gradient(#fafafa,#e9e9e9)" role="img" aria-label="Laptop, tablet and phone showing analytics dashboards"></div>
  <div class="tool-cap" style="left:164px">Tracking</div>
  <div class="tool-card" style="left:466px;background:linear-gradient(#fdfdfd,#ececec)" role="img" aria-label="Hand drawing a social media and marketing mind map"></div>
  <div class="tool-cap" style="left:466px">Market Research</div>
  <div class="tool-card" style="left:766px;background:linear-gradient(135deg,#8fd49a,#3fa451)" role="img" aria-label="Green analytics tools panel illustration"></div>
  <div class="tool-cap" style="left:766px">Analytics</div>
</div>

<!-- driving traffic -->
<h2 class="section-title" style="top:1246px">Driving Traffic</h2>
<div class="subtitle" style="top:1284px">Full service <span class="green">from beginning to end</span></div>

<div class="tbox" style="left:150px;top:1344px;height:232px">
  <div class="tbox-head">Prospecting Targeting</div>
  <ul><li>Target with dynamic creative ads</li><li>Maximise efficiency and costs with priority scoring</li><li>Individual bid per impression</li><li>Deliver your message across / brand</li></ul>
  <span class="learn">LEARN MORE &rarr;</span>
</div>
<div class="tbox" style="left:682px;top:1344px;height:232px">
  <div class="tbox-head">Re-Targeting</div>
  <ul><li>Target with dynamic creative ads</li><li>Maximise efficiency and costs with priority scoring</li><li>Individual bid per impression</li><li>Deliver your message across / brand</li></ul>
  <span class="learn">LEARN MORE &rarr;</span>
</div>
<div class="tbox" style="left:150px;top:1745px;height:224px">
  <div class="tbox-head">PPC</div>
  <ul><li>Customize ads according to search trends</li><li>Bespoke service to your needs and challenges</li><li>Easy and accurate measure of ROI</li><li>Continuous optimisation of running ads - we are Wrenmoor after all</li></ul>
  <span class="learn">LEARN MORE &rarr;</span>
</div>
<div class="tbox" style="left:682px;top:1745px;height:224px">
  <div class="tbox-head">Affiliate</div>
  <ul><li>Grow sales in a highly measurable and cost effective way.</li><li>Reach a wider audience across multiple channels</li><li>Building brand awareness</li><li>Pay only when a sale is confirmed Cost effective - paying only on confirmed sales</li></ul>
  <span class="learn">LEARN MORE &rarr;</span>
</div>
<svg class="abs" style="left:559px;top:1449px" width="82" height="20"><path d="M4 10h74M14 2 4 10l10 8M68 2l10 8-10 8" stroke="var(--green)" stroke-width="4" fill="none"/></svg>
<svg class="abs" style="left:559px;top:1847px" width="82" height="20"><path d="M4 10h74M14 2 4 10l10 8M68 2l10 8-10 8" stroke="var(--green)" stroke-width="4" fill="none"/></svg>
<svg class="abs" style="left:323px;top:1617px" width="20" height="82"><path d="M10 4v74M2 14l8-10 8 10M2 68l8 10 8-10" stroke="var(--green)" stroke-width="4" fill="none"/></svg>
<svg class="abs" style="left:855px;top:1617px" width="20" height="82"><path d="M10 4v74M2 14l8-10 8 10M2 68l8 10 8-10" stroke="var(--green)" stroke-width="4" fill="none"/></svg>
<div class="rule" style="top:2004px;background:#ccc"></div>

<!-- conversion chart -->
<h2 class="section-title" style="top:2034px">Conversion Optimisation</h2>
<div class="subtitle" style="top:2070px">Continuously <span class="green">increasing</span> your online</div>
<svg class="chart" width="968" height="326">
  <g transform="translate(0,6)">
  <g stroke="#e6e6e6" stroke-width="1">
    <line x1="27" y1="0" x2="968" y2="0"/><line x1="27" y1="50" x2="968" y2="50"/><line x1="27" y1="100" x2="968" y2="100"/><line x1="27" y1="150" x2="968" y2="150"/><line x1="27" y1="200" x2="968" y2="200"/><line x1="27" y1="250" x2="968" y2="250"/>
  </g>
  <g font-family="Lato, Arial, sans-serif" font-size="10" fill="#888" text-anchor="end">
    <text x="20" y="4">250</text><text x="20" y="54">200</text><text x="20" y="104">150</text><text x="20" y="154">100</text><text x="20" y="204">50</text><text x="20" y="254">0</text>
  </g>
  <g transform="translate(27,0)">
    <polygon fill="#e6ecef" points="0,259 74,232 139,218 205,232 267,213 333,185 395,164 469,131 532,104 600,82 668,68 736,55 796,95 867,55 941,82 941,296 0,296"/>
    <polyline fill="none" stroke="#c4ccd0" stroke-width="2" points="0,259 74,232 139,218 205,232 267,213 333,185 395,164 469,131 532,104 600,82 668,68 736,55 796,95 867,55 941,82"/>
    <polyline fill="none" stroke="var(--green)" stroke-width="3" points="0,232 74,224 139,245 205,267 267,177 333,251 395,150 469,82 532,136 600,68 668,164 736,27 796,205 867,27 941,218"/>
    <g fill="var(--green)"><circle cx="74" cy="224" r="4"/><circle cx="205" cy="267" r="4"/><circle cx="333" cy="251" r="4"/><circle cx="469" cy="82" r="4"/><circle cx="600" cy="68" r="4"/><circle cx="736" cy="27" r="4"/><circle cx="867" cy="27" r="4"/></g>
    <g stroke="#999" stroke-dasharray="3 3"><line x1="333" y1="165" x2="333" y2="251"/><line x1="532" y1="76" x2="532" y2="136"/><line x1="808" y1="60" x2="796" y2="205"/></g>
  </g>
  <g font-family="Lato, Arial, sans-serif" font-size="11" fill="#666" text-anchor="middle">
    <text x="30" y="314">Jan</text><text x="100" y="314">Feb</text><text x="166" y="314">Mar</text><text x="232" y="314">Apr</text><text x="294" y="314">May</text><text x="360" y="314">Jun</text><text x="422" y="314">Jul</text><text x="496" y="314">Aug</text><text x="559" y="314">Sep</text><text x="627" y="314">Oct</text><text x="695" y="314">Nov</text><text x="763" y="314">Dec</text>
  </g>
  </g>
</svg>
<div class="stats-box">
  <p>Increase sales without spending money on attracting more visitors</p>
  <p>Increase the overall user experience of your site</p>
  <p>Increase revenue by focusing visitors to your site</p>
  <b>LEARN MORE &rarr;</b>
</div>
<div class="callout" style="left:466px;top:2240px">A/B Testing</div>
<div class="callout" style="left:650px;top:2152px">Dynamic Content</div>
<div class="callout" style="left:908px;top:2140px">Pricing Module Testing</div>
<div class="rule" style="top:2446px;background:#ccc"></div>

<!-- personalisation flow -->
<div class="slide-arrow g" style="left:115px;top:2656px"><svg width="10" height="12"><path d="M8 1 2 6l6 5" stroke="#fff" stroke-width="2" fill="none"/></svg></div>
<div class="slide-arrow g" style="left:1053px;top:2656px"><svg width="10" height="12"><path d="M2 1l6 5-6 5" stroke="#fff" stroke-width="2" fill="none"/></svg></div>
<div class="pill" style="top:2558px;height:50px">Dynamic<br>Content</div>
<div class="pill" style="top:2628px;height:50px">A/B<br>Testing</div>
<div class="pill" style="top:2698px;height:70px">Consumer<br>Behaviour<br>Testing</div>
<svg class="abs" style="left:305px;top:2580px" width="71" height="10"><path d="M0 5h64M58 1l6 4-6 4" stroke="var(--green)" stroke-width="2" fill="none"/></svg>
<div class="panel">
  <div class="panel-title">Dynamic Content</div>
  <div class="ph" style="left:18px;top:72px;width:80px;height:66px;background:linear-gradient(135deg,#6b6b6b,#cfcfcf)" role="img" aria-label="Photo of a notebook and pen"></div>
  <p style="margin-left:90px">Lorem ipsum dolor sit amet, consectetur adipiscing elit, sed do eiusmod tempor incididunt ut labore et dolore magna aliqua.</p>
  <div style="margin-top:18px;height:76px;border:1px solid #ccc"></div>
  <p style="margin-top:8px">Lorem ipsum dolor sit amet, consectetur adipiscing elit, sed do eiusmod tempor incididunt ut.</p>
</div>
<svg class="abs" style="left:644px;top:2560px" width="166" height="220"><path d="M0 110h40M40 8v200M40 8h118M40 110h118M40 208h118M152 3l6 5-6 5M152 105l6 5-6 5M152 203l6 5-6 5" stroke="var(--green)" stroke-width="2" fill="none"/></svg>
<div class="persona" style="top:2530px"><div class="ph" style="left:8px;top:8px;width:46px;height:56px;background:linear-gradient(#d8b99b,#8a6a50)" role="img" aria-label="Portrait photo of a customer"></div><p>Lorem ipsum dolor sit amet, consectetur adipiscing elit</p></div>
<div class="persona" style="top:2626px"><div class="ph" style="left:8px;top:8px;width:46px;height:56px;background:linear-gradient(#e0c2a4,#94725a)" role="img" aria-label="Portrait photo of a customer"></div><p>Lorem ipsum dolor sit amet, consectetur adipiscing elit</p></div>
<div class="persona" style="top:2721px"><div class="ph" style="left:8px;top:8px;width:46px;height:56px;background:linear-gradient(#d4b497,#7b5e48)" role="img" aria-label="Portrait photo of a customer"></div><p>Lorem ipsum dolor sit amet, consectetur adipiscing elit</p></div>

<!-- projects -->
<div class="projects-band"></div>
<h2 class="section-title" style="top:2942px;color:var(--green)">Heroic Projects</h2>
<div class="projects-box"></div>
<div class="tab active" style="top:3019px">Conversion Optimisation</div>
<svg class="abs" style="left:423px;top:3019px" width="16" height="38"><path d="M0 0l16 19L0 38z" fill="var(--green)"/></svg>
<div class="tab" style="top:3076px">Social &amp; Content Marketing</div>
<div class="tab" style="top:3131px">Digital Marketing</div>
<div class="client" style="left:505px;top:3013px">Calder</div>
<div class="client" style="left:641px;top:3013px">Northwing</div>
<div class="client" style="left:777px;top:3013px">Pellory Media</div>
<div class="client" style="left:913px;top:3013px">Daily Lantern</div>
<div class="client" style="left:505px;top:3109px">Ostrand</div>
<div class="client" style="left:641px;top:3109px">Fizzberry</div>
<div class="client" style="left:777px;top:3109px">Harbourline Resorts</div>
<div class="client" style="left:913px;top:3109px">Vesper &amp; Co.</div>

<!-- articles -->
<article class="article" style="left:150px;top:3286px"><div class="article-body"><h4>Advanced Test / Mom &amp; Pop Test</h4><p>Proper optimisation requires specialist skills to create controlled experiments, alter copy, images, CTA, headline and content layout.</p><span class="more">SEE WHAT ADVANCED TESTING IS</span></div><div class="thumb" style="background:linear-gradient(135deg,#2e4e8a,#7fa0d6)" role="img" aria-label="Infographic about conversion testing"></div></article>
<article class="article" style="left:614px;top:3286px"><div class="article-body"><h4>Content Personalisation for ROI</h4><p>Using content personalisation to deliver targeted content to visitors based on interaction, behaviour and path.</p><span class="more">SEE WHAT ADVANCED TESTING IS</span></div><div class="thumb" style="background:linear-gradient(135deg,#c8202a,#f0a0a0)" role="img" aria-label="Infographic about personalising the web experience"></div></article>
<article class="article" style="left:150px;top:3458px"><div class="article-body"><h4>Download Our Media Manifesto</h4><p>Discover the difference between media optimisation and true end-to-end conversion planning, and the effects it has on your ROI.</p><span class="more">SEE WHAT ADVANCED TESTING IS</span></div><div class="thumb" style="background:linear-gradient(135deg,#3a7bbf,#a9cbe8)" role="img" aria-label="Laptop and devices showing the media manifesto"></div></article>
<article class="article" style="left:614px;top:3458px"><div class="article-body"><h4>Conversion Master Class</h4><p>Learn how to increase your online ROI by 50% through learning a couple of conversion fundamentals in just 2 hours.</p><span class="more">SEE WHAT ADVANCED TESTING IS</span></div><div class="thumb" style="background:linear-gradient(135deg,#5a4a3a,#c9a27c)" role="img" aria-label="Photo of a presenter at a master class"></div></article>
<article class="article" style="left:150px;top:3627px"><div class="article-body"><h4>Join The Family - We're Hiring!</h4><p>Whether you're a developer extraordinaire, savvy planner or marketing graduate we want to know how we can help you fulfil your career.</p><span class="more">SEE WHAT ADVANCED TESTING IS</span></div><div class="thumb" style="background:linear-gradient(135deg,#e6e6e6,#bdbdbd)" role="img" aria-label="We are hiring poster"></div></article>
<article class="article" style="left:614px;top:3627px"><div class="article-body"><h4>Subscription Marketers: Calculate LTV</h4><p>Download this free white paper written exclusively for subscription marketers that want to better understand the true value of a new subscriber.</p><span class="more">SEE WHAT ADVANCED TESTING IS</span></div><div class="thumb" style="background:linear-gradient(135deg,#f5f5f5,#c9d9ea)" role="img" aria-label="Lifetime value chart from a white paper"></div></article>

<!-- call to action -->
<section class="cta">
  <div class="ph" style="left:286px;top:-8px;width:290px;height:177px;background:linear-gradient(#4aa85a,#2f6e3a);opacity:.6" role="img" aria-label="Photo of three team members in business attire"></div>
  <div class="ph" style="left:804px;top:-8px;width:112px;height:177px;background:linear-gradient(#4aa85a,#2f6e3a);opacity:.6" role="img" aria-label="Photo of a team member presenting"></div>
  <h3>Wrenmoor Quill</h3>
  <div class="tag">Let the professionals do the work</div>
  <div class="btn">Meet the superheroes</div>
</section>
<footer class="site-footer">
  <span class="copy">&copy; Copyright 2013 Wrenmoor Quill &nbsp; | &nbsp; All Rights Reserved.</span>
  <nav><span>Our Service</span><span>Service</span><span>Client Work</span><span>Resources</span><span>Events</span><span>Contact Us</span><span>Blog</span></nav>
</footer>

</body>
</html>
```